Plumbing Company After Business Card

Business card for a plumbing business that offers a variety of plumbing services including maintenance, domestic and commercial plumbing. My main focus is to offer high quality professional service. A logo on the card would be ideal. Any other questions feel free to email. Cheers

Looking for something modern and upmarket with preferably a matte black background

Business name is Crestline Plumbing and Gas

Industry/Entity Type

Plumbing

Contact Information for Business Card

Crestline Plumbing and Gas
Marcus Thorvale
0472519306
14 Karrabee Drive, Linwood 3871
crestlineplumbing@mailbay.com.au
ABN 64 915 207 338

Font styles to use
Sans Serif

Colors
1b1b1b
ffffff
3377b5

Requirements
Must have
• Domestic
• Commercial
• Maintenance

```html
<!DOCTYPE html>
<html lang="en">
<head>
<meta charset="utf-8">
<title>Crestline Plumbing and Gas – Business Card</title>
<link rel="stylesheet" href="https://fonts.googleapis.com/css2?family=Lato:wght@300;400&display=swap">
<style>
  :root {
    --page-bg: #ffffff;
    --card-black: #1b1b1b;
    --card-deep: #0e0e0f;
    --card-edge: #2a2a2c;
    --brand-blue: #3377b5;
    --silver: #d6d8db;
    --text-white: #ffffff;
    --text-soft: #b9bcc0;
    --text-muted: #9a9ea3;
  }
  * { margin: 0; padding: 0; box-sizing: border-box; }
  html, body {
    width: 1200px;
    height: 900px;
    overflow: hidden;
    background: var(--page-bg);
    font-family: "Lato", Arial, sans-serif;
  }
  .stage {
    width: 1200px;
    height: 900px;
    display: flex;
    align-items: center;
    justify-content: center;
    gap: 40px;
  }
  .card {
    position: relative;
    width: 540px;
    height: 310px;
    border-radius: 22px;
    background:
      radial-gradient(ellipse at 50% 20%, var(--card-edge) 0%, var(--card-black) 45%, var(--card-deep) 100%);
    color: var(--text-white);
    overflow: hidden;
  }

  .brand {
    display: flex;
    align-items: center;
    justify-content: center;
    gap: 14px;
    color: var(--silver);
    font-weight: 400;
  }
  .brand-mark {
    width: 16px;
    height: 16px;
    background: var(--brand-blue);
    flex: none;
  }
  .brand-name {
    display: flex;
    flex-direction: column;
    align-items: flex-start;
    line-height: 1;
  }
  .brand-name .word { letter-spacing: 0.28em; }
  .brand-name .tagline { letter-spacing: 0.06em; margin-top: 6px; }

  .card-front .brand {
    position: absolute;
    top: 118px;
    left: 0;
    right: 0;
  }
  .card-front .brand-name .word { font-size: 34px; }
  .card-front .brand-name .tagline { font-size: 13px; }
  .services {
    position: absolute;
    left: 30px;
    right: 30px;
    bottom: 34px;
    display: flex;
    justify-content: space-between;
    list-style: none;
    font-size: 12px;
    font-weight: 400;
    letter-spacing: 0.22em;
    color: var(--text-soft);
  }

  .card-back .brand {
    position: absolute;
    top: 98px;
    left: 0;
    right: 0;
  }
  .card-back .brand-name .word { font-size: 26px; }
  .card-back .brand-name .tagline { font-size: 10px; }
  .divider {
    position: absolute;
    top: 170px;
    left: 0;
    right: 0;
    height: 2px;
    background: linear-gradient(90deg, rgba(214,216,219,0.35), var(--silver) 50%, rgba(214,216,219,0.35));
  }
  .contact {
    position: absolute;
    top: 190px;
    left: 0;
    right: 0;
    text-align: center;
    font-style: normal;
    font-weight: 300;
    line-height: 1.35;
  }
  .contact .person {
    font-size: 14px;
    font-weight: 400;
    letter-spacing: 0.06em;
    color: var(--text-white);
    margin-bottom: 8px;
  }
  .contact .phone {
    font-size: 14px;
    font-weight: 400;
    color: var(--text-white);
  }
  .contact .detail {
    font-size: 11px;
    color: var(--text-muted);
  }
</style>
</head>
<body>
  <main class="stage">
    <section class="card card-front" aria-label="Business card front">
      <div class="brand">
        <span class="brand-mark"></span>
        <div class="brand-name">
          <span class="word">CRESTLINE</span>
          <span class="tagline">PLUMBING AND GAS</span>
        </div>
      </div>
      <ul class="services">
        <li>DOMESTIC</li>
        <li>COMMERCIAL</li>
        <li>MAINTENANCE</li>
      </ul>
    </section>

    <section class="card card-back" aria-label="Business card back">
      <div class="brand">
        <span class="brand-mark"></span>
        <div class="brand-name">
          <span class="word">CRESTLINE</span>
          <span class="tagline">PLUMBING AND GAS</span>
        </div>
      </div>
      <div class="divider"></div>
      <address class="contact">
        <p class="person">MARCUS THORVALE</p>
        <p class="phone">0472519306</p>
        <p class="detail">14 Karrabee Drive, Linwood 3871</p>
        <p class="detail">crestlineplumbing@mailbay.com.au</p>
        <p class="detail">ABN 64 915 207 338</p>
      </address>
    </section>
  </main>
</body>
</html>
```